" Somos uma empresa do setor food truck. Trazemos um pedaço do nordeste do Brasil para as ruas e praças da Suíça. Especializado em tapioca recheada. Tapioca - a tendência da alimentação é sem glúten e sem lactose, quase não tem calorias e é super saborosa! Vendemos na hora do almoço em áreas industriais ou em emresarial. Prestamos serviço de catering para festas particulares, empresas e cantienas. No fim de semana vendemos nosso produto em grandes eventos, shows ou exposições "

```html
<!DOCTYPE html>
<html lang="pt">
<head>
<meta charset="utf-8">
<title>Cajuí Street-Food – Papel timbrado</title>
<link href="https://fonts.googleapis.com/css2?family=Oswald:wght@500;700&family=Open+Sans:wght@400;600&display=swap" rel="stylesheet">
<style>
  :root {
    --bg: #e9e9e9;
    --paper: #ffffff;
    --ink: #2b2b2b;
    --text: #555555;
    --brand: #8c2a1c;
    --accent: #e59a2f;
    --faint: #f3ece8;
  }
  * { margin: 0; padding: 0; box-sizing: border-box; }
  html, body { width: 1200px; height: 1200px; overflow: hidden; background: var(--bg); }
  .letterhead {
    position: absolute; left: 211px; top: 50px;
    width: 778px; height: 1100px;
    background: var(--paper);
    box-shadow: 0 4px 18px rgba(0,0,0,.12);
    font-family: "Open Sans", Arial, sans-serif;
    color: var(--text);
  }
  .brand {
    position: absolute; top: 62px; left: 370px;
    display: flex; align-items: center; gap: 12px;
  }
  .brand-dot { width: 34px; height: 34px; border-radius: 50%; background: var(--accent); }
  .brand-name {
    font-family: "Oswald", Arial, sans-serif; font-weight: 700;
    font-size: 40px; color: var(--brand); letter-spacing: 1px; line-height: 1;
  }
  .faint-mark {
    position: absolute; left: 220px; top: 360px;
    width: 340px; height: 340px; border-radius: 50%;
    background: var(--faint); opacity: .7;
  }
  .content { position: absolute; left: 80px; top: 180px; width: 618px; }
  .title {
    font-family: "Open Sans", Arial, sans-serif; font-weight: 600;
    font-size: 34px; color: var(--ink); margin-bottom: 22px; letter-spacing: 1px;
  }
  .content p { position: relative; font-size: 12.5px; line-height: 1.55; margin-bottom: 20px; }
  .signature {
    position: absolute; left: 300px; top: 880px; width: 180px; text-align: center;
  }
  .signature-mark { width: 120px; height: 50px; margin: 0 auto 4px; border-radius: 6px;
    background: linear-gradient(90deg, #e6e6e6, #cfcfcf); }
  .signature-name { font-size: 12px; color: var(--ink); border-top: 1px solid var(--ink); padding-top: 4px; }
  .signature-role { font-size: 10px; color: var(--accent); }
  .footer-rule { position: absolute; left: 50px; right: 50px; top: 1010px; height: 2px; background: var(--ink); }
  .contacts {
    position: absolute; left: 50px; right: 50px; top: 1030px;
    display: flex; justify-content: space-between; align-items: center;
    font-family: "Oswald", Arial, sans-serif; font-weight: 500;
    font-size: 14px; color: var(--brand); letter-spacing: 1px; text-transform: uppercase;
  }
  .contact { display: flex; align-items: center; gap: 6px; }
  .contact svg { width: 16px; height: 16px; fill: var(--accent); }
  .address { line-height: 1.15; }
</style>
</head>
<body>
<main class="letterhead">
  <div class="brand">
    <span class="brand-dot"></span>
    <span class="brand-name">Cajuí Street-Food</span>
  </div>

  <div class="faint-mark" aria-hidden="true"></div>

  <section class="content">
    <h1 class="title">TÍTULO</h1>
    <p>Lorem Ipsum é simplesmente uma simulação de texto da indústria tipográfica e de impressos, e vem sendo utilizado desde o século XVI, quando um impressor desconhecido pegou uma bandeja de tipos e os embaralhou para fazer um livro de modelos de tipos. Lorem Ipsum sobreviveu não só a cinco séculos, como também ao salto para a editoração eletrônica, permanecendo essencialmente inalterado. Se popularizou na década de 60, quando a Letraset lançou decalques contendo passagens de Lorem Ipsum, e mais recentemente quando passou a ser integrado a softwares de editoração eletrônica como Aldus PageMaker.</p>
    <p>Lorem Ipsum é simplesmente uma simulação de texto da indústria tipográfica e de impressos, e vem sendo utilizado desde o século XVI, quando um impressor desconhecido pegou uma bandeja de tipos e os embaralhou para fazer um livro de modelos de tipos. Lorem Ipsum sobreviveu não só a cinco séculos, como também ao salto para a editoração eletrônica, permanecendo essencialmente inalterado. Se popularizou na década de 60, quan</p>
    <p>Lorem Ipsum é simplesmente uma simulação de texto da indústria tipográfica e de impressos, e vem sendo utilizado desde o século XVI, quando um impressor desconhecido pegou uma bandeja de tipos e os embaralhou para fazer</p>
    <p>Lorem Ipsum é simplesmente uma simulação de texto da indústria tipográfica e de impressos, e vem sendo utilizado desde o século XVI, quando um impressor desconhecido pegou uma bandeja de tipos e os embaralhou para fazer</p>
    <p>Lorem Ipsum é simplesmente uma simulação de texto da indústria tipográfica e de impressos, e vem sendo utilizado desde o século XVI, quando um impressor desconhecido pegou uma bandeja de tipos e os embaralhou para fazer</p>
  </section>

  <div class="signature">
    <div class="signature-mark" role="img" aria-label="Assinatura manuscrita do responsável"></div>
    <div class="signature-name">Nome Responsável</div>
    <div class="signature-role">Cargo</div>
  </div>

  <div class="footer-rule"></div>
  <footer class="contacts">
    <span class="contact">
      <svg viewBox="0 0 24 24"><path d="M6.6 10.8a15 15 0 0 0 6.6 6.6l2.2-2.2a1 1 0 0 1 1-.25 11.4 11.4 0 0 0 3.6.57 1 1 0 0 1 1 1V20a1 1 0 0 1-1 1A17 17 0 0 1 3 4a1 1 0 0 1 1-1h3.5a1 1 0 0 1 1 1c0 1.25.2 2.45.57 3.6a1 1 0 0 1-.25 1z"/></svg>
      +41 76 000 12 34
    </span>
    <span class="contact">
      <svg viewBox="0 0 24 24"><path d="M2 5h20v14H2z M2 5l10 8 10-8" fill="none" stroke="#e59a2f" stroke-width="2"/></svg>
      ola@cajui.ch
    </span>
    <span class="contact">
      <svg viewBox="0 0 24 24"><circle cx="12" cy="12" r="9" fill="none" stroke="#e59a2f" stroke-width="2"/><path d="M3 12h18M12 3c3 3 3 15 0 18M12 3c-3 3-3 15 0 18" fill="none" stroke="#e59a2f" stroke-width="1.6"/></svg>
      www.cajui.ch
    </span>
    <span class="contact">
      <svg viewBox="0 0 24 24"><path d="M12 2a7 7 0 0 0-7 7c0 5 7 13 7 13s7-8 7-13a7 7 0 0 0-7-7zm0 9.5A2.5 2.5 0 1 1 12 6.5a2.5 2.5 0 0 1 0 5z"/></svg>
      <span class="address">Lindenweg 12<br>CH-4051 Basel</span>
    </span>
  </footer>
</main>
</body>
</html>
```